KV Group

We need a new website for our company and since we had a very good work done for our logo in this site, we're back for the entire job.

Our company name is Marlowe Capital Group. We're adding files of examples of what we have done today. In my opinion we need a more attention lock in the site but yet financial simple work.

Our files (attached) will let you know what we have so far. We need a complete change but the colours should be the same, however you can change them not running away to far from the original, and of course matching with the logo.

We need examples for 3 kind of layouts.

- A HOME welcome layout
- An internal Layout with sidebar
- And internal Layout wide

We can buy image licenses if needed for assets.
Actually there are 5 slide images placed on the Welcome HOME, we need those there, but you can improve with better images to match the new website!!!

Target Market(s)

Clients looking for financial advisers, tax and funds specialist, currency advisers

Industry/Entity Type

Financial

Requirements
Must have
• all the fonts must be in accordance with the financial market sites........the welcome home page must be precise, neat and information accurate........the menu should be elegant........main focus on the Home page, should be also the PRIVATE ACCESS box log in.......

```html
<!DOCTYPE html>
<html lang="en">
<head>
<meta charset="utf-8">
<title>Marlowe Capital Group</title>
<link href="https://fonts.googleapis.com/css2?family=Oswald:wght@300;400&display=swap" rel="stylesheet">
<style>
:root{
  --orange:#f47a20;
  --orange-soft:rgba(244,122,32,.85);
  --ink:#222;
  --text:#333;
  --page:#f3f3f3;
  --white:#fff;
  --footer:#231f20;
  --footer-low:#333132;
  --up:#1a8f6a;
  --down:#e0262b;
}
*{box-sizing:border-box;margin:0;padding:0}
html,body{width:1099px;height:1200px;overflow:hidden}
body{background:var(--page);font-family:Arial,Helvetica,sans-serif;color:var(--text);position:relative}
.abs{position:absolute}
.display{font-family:'Oswald',sans-serif;font-weight:300;text-transform:uppercase}
.backdrop{left:0;top:0;width:1099px;height:420px;background:linear-gradient(120deg,#3c4d62 0%,#7b8a98 35%,#b9b2aa 60%,#7d2a28 85%,#4a5a6c 100%)}
.topbar{left:229px;top:0;width:641px;height:24px;background:var(--orange);display:flex;justify-content:flex-end;align-items:center;gap:14px;padding-right:13px}
.topbar a{color:var(--white);text-decoration:none;font-size:12px;display:flex;align-items:center;gap:5px}
.header{left:229px;top:34px;width:641px;height:72px;background:var(--white);overflow:hidden}
.brand{position:absolute;left:8px;top:10px;width:140px;text-align:center}
.brand-mark{width:40px;height:26px;background:var(--orange);margin:0 auto 6px}
.brand-name{font-family:'Oswald',sans-serif;font-weight:400;font-size:11px;color:var(--ink);letter-spacing:.5px;text-transform:uppercase}
.nav{position:absolute;left:154px;top:0;height:72px;display:flex}
.nav a{font-family:'Oswald',sans-serif;font-size:12.5px;color:var(--ink);text-decoration:none;line-height:72px;padding:0 9px;text-transform:uppercase}
.nav a.active{background:var(--orange);color:var(--white);padding:0 9px}
.search{position:absolute;right:0;top:0;width:54px;height:62px;background:var(--orange);border-bottom-left-radius:54px}
.hero{left:229px;top:118px;width:641px;height:207px;background:linear-gradient(100deg,#d9cfc3 0%,#b6a89a 45%,#6d6a78 75%,#8b6d5e 100%)}
.hero-title{left:248px;top:218px;width:220px;height:38px;background:rgba(255,255,255,.88);color:var(--orange);font-size:21px;line-height:38px;padding-left:11px}
.hero-sub{left:248px;top:256px;width:274px;height:30px;background:var(--orange-soft);color:var(--white);font-size:8.5px;line-height:11px;padding:5px 12px}
.btn{background:var(--ink);color:var(--white);font-family:'Oswald',sans-serif;font-size:10px;text-transform:uppercase;text-align:center;line-height:20px;height:20px}
.welcome{left:229px;top:338px;width:420px;height:141px;background:var(--white);border:1px solid #bdbdbd;padding:8px 12px}
.welcome h1{font-family:'Oswald',sans-serif;font-weight:300;font-size:21px;color:var(--ink);text-transform:uppercase;margin-bottom:10px}
.welcome h1 span{color:var(--orange)}
.copy{font-size:7.6px;line-height:12.8px;color:var(--text)}
.private{left:671px;top:338px;width:199px;height:141px;background:var(--orange);padding:8px 10px}
.private h2{font-family:'Oswald',sans-serif;font-weight:400;color:var(--white);font-size:21px;text-align:center;text-transform:uppercase;margin-bottom:8px}
.field{width:180px;height:20px;background:var(--white);border:1px solid #e6e6e6;margin-bottom:8px}
.forgot{font-size:7.6px;color:#fde6d2;margin-top:-1px}
.private .btn{width:92px;margin-top:8px}
.card{top:498px;width:199px;height:142px;border:1px solid #ccc}
.card-art{width:100%;height:100%}
.card-band{position:absolute;left:0;bottom:0;width:100%;height:34px;background:var(--orange-soft);color:var(--white);font-family:'Oswald',sans-serif;font-size:15px;line-height:34px;padding-left:12px;text-transform:uppercase}
.card-copy{top:648px;width:200px}
.card-btn{top:718px;width:57px}
.ticker{left:229px;top:758px;width:641px;height:23px;background:#f7f6f4;border:1px solid #cfcfcf;font-size:8px;line-height:22px;text-align:center;word-spacing:1px}
.ticker .up{color:var(--up)}.ticker .down{color:var(--down)}
.ticker span.pair{margin:0 7px}
.verified{left:229px;top:800px;width:641px;text-align:center;font-size:19px;color:var(--ink)}
.badges{left:375px;top:836px;display:flex;gap:28px;align-items:center}
.footer{left:0;top:907px;width:1099px;height:175px;background:var(--footer)}
.footer-low{left:0;top:1082px;width:1099px;height:118px;background:var(--footer-low)}
.fcol{top:918px}
.fcol h3{font-family:'Oswald',sans-serif;font-weight:300;color:var(--orange);font-size:17px;text-transform:uppercase;margin-bottom:9px}
.fcol ul{list-style:none}
.fcol li{font-size:8px;line-height:12.8px;color:#ddd}
.fcol h3.second{margin-top:6px}
.legal{left:242px;top:1092px;width:616px;font-size:7.6px;line-height:12.8px;color:#e6e6e6}
.copyright{left:242px;top:1172px;font-size:7.6px;color:#e6e6e6}
</style>
</head>
<body>
<div class="abs backdrop" role="img" aria-label="Blurred background photo of financial charts and a dotted world map"></div>

<div class="abs topbar">
  <a href="#"><svg width="13" height="13" viewBox="0 0 13 13"><rect x="1" y="2" width="9" height="10" fill="none" stroke="#fff" stroke-width="1.2"/><path d="M5 8 L11 2" stroke="#fff" stroke-width="1.5"/></svg>APPLE NOW</a>
  <a href="#"><svg width="15" height="12" viewBox="0 0 15 12"><rect x="1" y="3" width="13" height="8" fill="none" stroke="#fff" stroke-width="1.2"/><path d="M1 3 L7.5 8 L14 3 M2 3 L7.5 0.5 L13 3" fill="none" stroke="#fff" stroke-width="1.2"/></svg>CONTACT US</a>
</div>

<header class="abs header">
  <div class="brand"><div class="brand-mark"></div><div class="brand-name">Marlowe Capital Group</div></div>
  <nav class="nav">
    <a class="active" href="#">Home</a><a href="#">About us</a><a href="#">Investments</a><a href="#">Funds</a><a href="#">Brokerage</a><a href="#">Exchange</a><a href="#">Accounts</a>
  </nav>
  <div class="search"><svg width="54" height="62" viewBox="0 0 54 62"><circle cx="31" cy="26" r="10" fill="none" stroke="#fff" stroke-width="3"/><path d="M24 33 L14 43" stroke="#fff" stroke-width="4" stroke-linecap="round"/></svg></div>
</header>

<div class="abs hero" role="img" aria-label="Photo of two smiling advisers in a bright modern office with a glass roof and staircase"></div>
<div class="abs hero-title display">Find your own solution</div>
<div class="abs hero-sub">Find the way of saving and investing that Suits you Best.<br>We will help you understand your situation and your potential.</div>
<div class="abs btn" style="left:248px;top:289px;width:57px">Read more</div>

<section class="abs welcome">
  <h1><span>Welcome to</span> Marlowe Capital Group.</h1>
  <p class="copy"><b>Lorem Ipsum</b> is simply dummy text of the printing and typesetting industry. Lorem Ipsum has been the industry's standard dummy text ever since the 1500s, when an unknown printer took a galley of type and scrambled it to make a type specimen book. It has survived not only five centuries, but also the leap into electronic typesetting, remaining essentially unchanged. It was popularised in the 1960s with the release of Letraset sheets containing Lorem Ipsum passages, and more recently with desktop publishing software like Aldus PageMaker including versions of Lorem Ipsum.</p>
</section>

<section class="abs private">
  <h2>Private access</h2>
  <div class="field"></div>
  <div class="field"></div>
  <p class="forgot">Forget acc number / password?</p>
  <div class="btn">Log in to accounts</div>
</section>

<div class="abs card" style="left:229px"><div class="card-art" role="img" aria-label="Bronze gears with currency symbols" style="background:linear-gradient(135deg,#5a3a22,#c79a6c,#3b2616)"></div><div class="card-band">Managmeent &amp; Strategy</div></div>
<div class="abs card" style="left:450px"><div class="card-art" role="img" aria-label="Photo of a smiling woman at an office desk" style="background:linear-gradient(135deg,#e8e6e2,#b9a58c,#7f7366)"></div><div class="card-band">Funds</div></div>
<div class="abs card" style="left:671px"><div class="card-art" role="img" aria-label="Magnifying glass over currency exchange chart printout" style="background:linear-gradient(135deg,#d8d8d6,#9fa4a6,#e9e9e6)"></div><div class="card-band">Currency Fexchange</div></div>

<p class="abs copy card-copy" style="left:229px"><b>Lorem Ipsum</b> is simply dummy text of the printing and typesetting industry. Lorem Ipsum has been the industry's standard dummy text ever since the 1500s, when an unknown printer took a galley of type and scrambled it to make a type specimen book.</p>
<p class="abs copy card-copy" style="left:450px"><b>Lorem Ipsum</b> is simply dummy text of the printing and typesetting industry. Lorem Ipsum has been the industry's standard dummy text ever since the 1500s, when an unknown printer took a galley of type and scrambled it to make a type specimen book.</p>
<p class="abs copy card-copy" style="left:671px"><b>Lorem Ipsum</b> is simply dummy text of the printing and typesetting industry. Lorem Ipsum has been the industry's standard dummy text ever since the 1500s, when an unknown printer took a galley of type and scrambled it to make a type specimen book.</p>
<div class="abs btn card-btn" style="left:229px">Read more</div>
<div class="abs btn card-btn" style="left:450px">Read more</div>
<div class="abs btn card-btn" style="left:671px">Read more</div>

<div class="abs ticker">
  <span class="pair">GBP/EUR = <span class="up">1.18833 ▲</span></span>
  <span class="pair">GBP/AUD = <span class="up">1.70716 ▲</span></span>
  <span class="pair">GBP/CAD = <span class="down">1.63763 ▼</span></span>
  <span class="pair">GBP/USD = <span class="down">1.5586 ▼</span></span>
  <span class="pair">GBP/NZD = <span class="down">1.97482 ▼</span></span>
  <span class="pair">GBP/TRY = <span class="up">3.22321 ▲</span></span>
</div>

<h2 class="abs verified display">Verified and protected by</h2>
<div class="abs badges">
  <svg width="88" height="36"><rect x="0" y="6" width="88" height="24" rx="3" fill="#c9c9c9"/></svg>
  <svg width="36" height="36"><circle cx="18" cy="18" r="17" fill="#2b4a8a"/></svg>
  <svg width="78" height="30"><rect width="78" height="30" fill="#1f4fa0"/></svg>
  <svg width="110" height="32"><rect width="32" height="32" rx="4" fill="#6bb33a"/></svg>
</div>

<footer>
  <div class="abs footer"></div>
  <div class="abs fcol" style="left:242px"><h3>About</h3><ul><li>History</li><li>Expertiza</li><li>Identity</li><li>Strategy</li><li>Contact us</li></ul></div>
  <div class="abs fcol" style="left:344px"><h3>Invefstments</h3><ul><li>Term Defposits</li><li>Managment &amp; Strategy</li><li>Client Relations</li><li>Financial Privacy</li><li>Tax Advice</li><li>Wealth Analysis &amp; Financial Planning</li><li>Active Advisory Group</li><li>Manager Selection Services</li><li>Private Equity</li></ul></div>
  <div class="abs fcol" style="left:513px"><h3>Funds</h3><ul><li>Overview</li><li>Administration</li><li>Funds Security</li><li>Core Services</li><li>Reporting</li><li>Revenue oportunities</li><li>How it works?</li><li>Glossary</li></ul></div>
  <div class="abs fcol" style="left:623px"><h3>Currency exchange</h3><ul><li>Foreign Exchange</li><li>Fx Forward</li><li>Fx Options</li></ul><h3 class="second">Accounts</h3><ul><li>Apply Now</li><li>Private Access</li></ul></div>
  <div class="abs fcol" style="left:788px"><h3>Brokerage</h3><ul><li>Institutional</li><li>Research</li><li>Trading</li></ul></div>
  <div class="abs footer-low"></div>
  <p class="abs legal">Lorem Ipsum is simply dummy text of the printing and typesetting industry. Lorem Ipsum has been the industry's standard dummy text ever since the 1500s, when an unknown printer took a galley of type and scrambled it to make a type specimen book. It has survived not only five centuries, but also the leap into electronic typesetting, remaining essentially unchanged. It was popularised in the 1960s with the release of Letraset sheets containing Lorem Ipsum passages, and more recently with desktop publishing software like Aldus PageMaker including versions of Lorem Ipsum.</p>
  <p class="abs copyright">© Marlowe Capital 2013</p>
</footer>
</body>
</html>
```